Web Page needed for Dr. Brannock Advisory

The company works in the consultant business for processes in large projects our of engineering and construction business. We develop strategies but work also in critical projects to get them right.
The page should have a modern appearance but though a classy and luxury touch.
Updates

The project was bought in a package, logo plus web page. Now the designers do submit logos again, although the logo has been set. This part is only the web site. I changed the text to clarify it, I contacted support to put that right, but that needs an extension of minimum 7 days to catch up.

Due to the confusion in the project, it was first set up as logo project and later corrected (I have no clue how that happened, as I bought a package with logo + web, and logo is already done), there is a large delay in getting feedback. Please be so kind and extend until 31.01. In Europe there is holidays until 07.01. and I have no time to discuss the topics with my client until 10.01., than we need to feed in response and get changes done.

Logo Text

The logo is already fixed, I asked for web page.

Number of Pages Required

5+ page

Font styles to use
Sans Serif

Colors

Designer to choose colors to be used in the design.

Requirements
Must have
• Home/Start
• Lean Construction
• Lean Equipment
• Lean Design
• Lean Training
• Team
• Contact
• Imprint
Nice to have
• Darker color, luxury appearance, please integrate the logo in the attachment here.
• I would like to have a web page with animated context, such as this one here: https://quellworks.example

```html
<!DOCTYPE html>
<html lang="en">
<head>
<meta charset="utf-8">
<title>Dr. Brannock Advisory</title>
<link href="https://fonts.googleapis.com/css2?family=Mulish:wght@400;600;700;800&display=swap" rel="stylesheet">
<style>
:root{
  --green:#7dbb2e;
  --green-dark:#5f9a1c;
  --blue:#1f4f9a;
  --blue-dark:#153a75;
  --ink:#1b1d20;
  --bg-1:#0d1116;
  --bg-2:#131a22;
  --bg-3:#0a0e12;
  --bg-footer:#0c1015;
  --text-soft:#9aa3ad;
  --line:#2b333d;
  --white:#ffffff;
}
*{box-sizing:border-box;margin:0;padding:0}
html,body{width:1200px;height:2928px;overflow:hidden}
body{font-family:"Mulish",sans-serif;background:var(--bg-1);color:var(--white);position:relative}
section,header,footer{position:absolute;left:0;width:1200px}
a{color:inherit;text-decoration:none}

/* header */
.site-header{top:0;height:72px;z-index:5}
.nav-bar{position:absolute;left:0;top:0;width:1200px;height:34px;background:linear-gradient(90deg,var(--blue-dark),var(--blue))}
.brand{position:absolute;left:0;top:0;width:352px;height:72px;background:var(--white);display:flex;align-items:center;gap:14px;padding-left:30px}
.brand-mark{width:30px;height:30px;background:var(--blue)}
.brand-name{font-weight:800;font-size:22px;color:var(--blue);letter-spacing:.5px}
.main-nav{position:absolute;left:596px;top:0;height:34px;display:flex;gap:34px;align-items:center;font-size:12px;font-weight:700;letter-spacing:1px}
.main-nav a{height:34px;line-height:34px;padding:0 8px}
.main-nav a.is-active{background:var(--green)}

/* hero */
.hero{top:0;height:608px}
.hero-photo{position:absolute;inset:0;background:linear-gradient(160deg,#dfe6ec 0%,#b9c3cb 40%,#8e8579 70%,#6d6254 100%)}
.hero-copy{position:absolute;right:134px;top:104px;width:420px;text-align:right}
.hero-copy h1{font-size:25px;line-height:31px;font-weight:800;color:var(--ink)}
.btn{display:inline-block;font-size:12px;font-weight:700;letter-spacing:1px;padding:11px 18px}
.btn-solid{background:var(--green);color:var(--ink)}
.btn-outline{border:1px solid #6a737d;color:#d9dee3}
.hero-copy .btn{margin-top:20px}
.slider-arrow{position:absolute;top:326px;width:34px;height:34px;background:rgba(20,24,30,.8);display:flex;align-items:center;justify-content:center}
.slider-arrow.prev{left:48px}
.slider-arrow.next{right:48px}

/* welcome */
.welcome{top:608px;height:464px;background:var(--bg-1)}
.welcome-copy{position:absolute;left:144px;top:96px;width:470px}
h2.section-heading{font-size:32px;font-weight:700;color:var(--green);line-height:40px}
.body-text{font-size:13px;line-height:22px;color:var(--text-soft);margin:18px 0 24px}
.logo-panel{position:absolute;left:700px;top:-28px;width:352px;height:348px;background:#eef0f2;display:flex;align-items:center;justify-content:center;gap:14px}
.logo-frame{position:absolute;left:676px;top:-4px;width:392px;height:360px;border:2px solid var(--green)}
.logo-panel .brand-mark{width:40px;height:40px}
.logo-panel .brand-name{font-size:24px}

/* processes */
.processes{top:1072px;height:416px;background:var(--bg-2)}
.process-frame{position:absolute;left:160px;top:-24px;width:364px;height:368px;border:2px solid var(--green)}
.process-photo{position:absolute;left:144px;top:-40px;width:360px;height:360px;background:linear-gradient(150deg,#8fb5d4 0%,#c9c7a5 45%,#d8c04a 70%,#6d7783 100%)}
.process-copy{position:absolute;left:592px;top:40px;width:460px}

/* projects */
.projects{top:1488px;height:832px;background:var(--bg-3)}
.projects h2{text-align:center;position:absolute;top:68px;width:100%}
.project-grid{position:absolute;left:144px;top:136px;width:912px;height:568px;display:grid;grid-template-columns:1fr 1fr;grid-template-rows:1fr 1fr;gap:8px}
.project-tile{display:block}
.tile-1{background:linear-gradient(160deg,#6fa6d6,#c9a874 60%,#8a6a44)}
.tile-2{background:linear-gradient(160deg,#3f86cf,#a8c6e2 55%,#d9e3ec)}
.tile-3{background:linear-gradient(160deg,#7b8792,#c3ccd4 50%,#5d6a76)}
.tile-4{background:linear-gradient(160deg,#2d4f7d,#6c8cb3 50%,#1d2e46)}
.grid-badge{position:absolute;left:568px;top:388px;width:64px;height:64px;border-radius:50%;background:var(--white);border:4px solid var(--bg-3)}
.projects .btn{position:absolute;left:548px;top:722px}

/* contact */
.contact{top:2320px;height:480px;background:var(--bg-1)}
.contact h2{position:absolute;top:76px;width:100%;text-align:center}
.contact-form{position:absolute;left:144px;top:128px;width:440px}
.field-row{display:flex;gap:8px;margin-bottom:8px}
.field{flex:1;height:38px;border:1px solid var(--line);background:#11171e;font-size:11px;color:var(--text-soft);padding:11px 12px}
.field.message{height:140px}
.contact-form .btn{margin-top:8px}
.map{position:absolute;left:612px;top:132px;width:444px;height:220px;background:linear-gradient(135deg,#c7ccd1,#e3e6e9 50%,#b4bac0)}
.contact-info{position:absolute;left:612px;top:372px;font-size:12px;line-height:24px;color:var(--text-soft)}
.contact-info li{list-style:none;display:flex;align-items:center;gap:10px}

/* footer */
.site-footer{top:2800px;height:128px;background:var(--bg-footer);border-top:1px solid var(--line)}
.footer-nav{position:absolute;left:144px;top:44px;display:flex;gap:16px;font-size:11px;color:var(--text-soft)}
.copyright{position:absolute;left:144px;top:70px;font-size:11px;color:#6f7882}
.social{position:absolute;right:144px;top:52px;display:flex;gap:14px}
.social span{width:22px;height:22px;border-radius:50%;background:#5f6a75}
</style>
</head>
<body>

<header class="site-header">
  <div class="nav-bar"></div>
  <a class="brand" href="#"><span class="brand-mark"></span><span class="brand-name">Dr. Brannock Advisory</span></a>
  <nav class="main-nav">
    <a class="is-active" href="#">HOME</a>
    <a href="#">SERVICES</a>
    <a href="#">PROJECTS</a>
    <a href="#">ABOUT US</a>
    <a href="#">CONTACT US</a>
  </nav>
</header>

<section class="hero">
  <div class="hero-photo" role="img" aria-label="Concrete building under construction with tower cranes and a worker on scaffolding"></div>
  <div class="hero-copy">
    <h1>Consultant business for Processes in Large Projects of Engineering and Construction Business</h1>
    <a class="btn btn-solid" href="#">READ MORE</a>
  </div>
  <a class="slider-arrow prev" href="#" aria-label="Previous slide"><svg width="12" height="14" viewBox="0 0 12 14"><path d="M9 1 3 7l6 6" fill="none" stroke="#fff" stroke-width="2"/></svg></a>
  <a class="slider-arrow next" href="#" aria-label="Next slide"><svg width="12" height="14" viewBox="0 0 12 14"><path d="m3 1 6 6-6 6" fill="none" stroke="#fff" stroke-width="2"/></svg></a>
</section>

<section class="welcome">
  <div class="welcome-copy">
    <h2 class="section-heading">Welcome to Dr. Brannock Advisory</h2>
    <p class="body-text">We guide owners and contractors through complex engineering and construction programmes. Our advisors structure processes, align teams and bring critical projects back on track with lean methods, clear planning and steady leadership from the first concept to the final handover on site.</p>
    <a class="btn btn-outline" href="#">READ MORE</a>
  </div>
  <div class="logo-frame"></div>
  <div class="logo-panel"><span class="brand-mark"></span><span class="brand-name">Dr. Brannock Advisory</span></div>
</section>

<section class="processes">
  <div class="process-frame"></div>
  <div class="process-photo" role="img" aria-label="Engineers in hard hats and safety vests reviewing plans on a table"></div>
  <div class="process-copy">
    <h2 class="section-heading">Consultant Business for Processes</h2>
    <p class="body-text">From lean design to lean equipment and training, we build processes that fit large projects. We develop strategies, measure progress and work side by side with your people until every phase runs reliably, on time and within budget.</p>
    <a class="btn btn-outline" href="#">READ MORE</a>
  </div>
</section>

<section class="projects">
  <h2 class="section-heading">Our Projects</h2>
  <div class="project-grid">
    <div class="project-tile tile-1" role="img" aria-label="Building site with yellow tower cranes"></div>
    <div class="project-tile tile-2" role="img" aria-label="Workers assembling a steel roof structure"></div>
    <div class="project-tile tile-3" role="img" aria-label="Steel hall frame with a crane"></div>
    <div class="project-tile tile-4" role="img" aria-label="Steel lattice roof seen from below"></div>
  </div>
  <div class="grid-badge"></div>
  <a class="btn btn-outline" href="#">VIEW ALL</a>
</section>

<section class="contact">
  <h2 class="section-heading">Contact Us</h2>
  <form class="contact-form">
    <div class="field-row"><div class="field">Name</div><div class="field">Email</div></div>
    <div class="field-row"><div class="field">Phone</div><div class="field">Fax</div></div>
    <div class="field-row"><div class="field message">Message</div></div>
    <a class="btn btn-solid" href="#">SUBMIT</a>
  </form>
  <div class="map" role="img" aria-label="Street map showing the office location"></div>
  <ul class="contact-info">
    <li><svg width="10" height="14" viewBox="0 0 10 14"><path d="M5 0a5 5 0 0 0-5 5c0 4 5 9 5 9s5-5 5-9a5 5 0 0 0-5-5Zm0 7a2 2 0 1 1 0-4 2 2 0 0 1 0 4Z" fill="#7dbb2e"/></svg>14 Harbour Lane, Eastgate, Northfield 40210</li>
    <li><svg width="12" height="12" viewBox="0 0 12 12"><path d="M2.5 0 4.5 3 3 4.5a8 8 0 0 0 4.5 4.5L9 7.5l3 2L10.5 12C5 12 0 7 0 1.5Z" fill="#7dbb2e"/></svg>+49 000 555 0199</li>
    <li><svg width="13" height="10" viewBox="0 0 13 10"><rect x=".5" y=".5" width="12" height="9" fill="none" stroke="#7dbb2e"/><path d="m.5.5 6 5 6-5" fill="none" stroke="#7dbb2e"/></svg>info@brannockadvisory.example</li>
  </ul>
</section>

<footer class="site-footer">
  <nav class="footer-nav"><a href="#">Home</a><a href="#">Services</a><a href="#">Projects</a><a href="#">About Us</a><a href="#">Contact Us</a></nav>
  <p class="copyright">Copyright © 2019 Dr. Brannock Advisory</p>
  <div class="social"><span></span><span></span></div>
</footer>

</body>
</html>
```